Bramwell Ridge Minerals

Looking for a cool, glossy business card...white with our logo on one side and then the a smaller version of the logo on the other side (top left hand corner) and then the name and position of the person next to it, and then the office address and email address on the bottom left hand corner and the phone numbers & email address on the bottom right hand corner. I have the logo already...can pass it on when you're ready.

```html
<!DOCTYPE html>
<html lang="en">
<head>
<meta charset="utf-8">
<title>Bramwell Ridge Minerals – Business Card</title>
<link href="https://fonts.googleapis.com/css2?family=Cinzel:wght@400;600&family=Montserrat:wght@400;500&display=swap" rel="stylesheet">
<style>
  :root {
    --bg: #5a5c5f;
    --card-white: #ffffff;
    --card-dark: #3a3d42;
    --ink: #2a2b2e;
    --silver: #b9bcc1;
    --name-blue: #2c3bb0;
    --text-light: #f2f2f2;
    --accent-red: #d31f2b;
  }
  * { box-sizing: border-box; margin: 0; padding: 0; }
  html, body { width: 1200px; height: 965px; overflow: hidden; }
  body {
    background: var(--bg);
    font-family: "Montserrat", sans-serif;
    position: relative;
  }
  .card {
    position: absolute;
    left: 210px;
    width: 780px;
    height: 446px;
    box-shadow: 0 10px 28px rgba(0,0,0,.35);
  }
  .card--front { top: 24px; background: var(--card-white); }
  .card--back { top: 495px; background: var(--card-dark); color: var(--text-light); }

  .brand {
    font-family: "Cinzel", serif;
    font-weight: 400;
    display: flex;
    align-items: center;
    gap: 14px;
    white-space: nowrap;
  }
  .brand__dot { border-radius: 50%; flex: none; }

  .card--front .brand {
    position: absolute;
    left: 0; right: 0; top: 190px;
    justify-content: center;
    font-size: 44px;
    color: var(--ink);
    letter-spacing: 1px;
  }
  .card--front .brand__dot { width: 22px; height: 22px; background: var(--ink); }

  .card--back .brand {
    position: absolute;
    left: 44px; top: 40px;
    font-size: 26px;
    color: var(--silver);
    gap: 10px;
  }
  .card--back .brand__dot { width: 13px; height: 13px; background: var(--silver); }

  .person { position: absolute; left: 44px; top: 236px; }
  .person__name {
    font-family: "Cinzel", serif;
    font-size: 34px;
    color: var(--name-blue);
    letter-spacing: 1px;
    line-height: 1.1;
  }
  .person__role { font-size: 20px; margin-top: 4px; }

  .contact { position: absolute; list-style: none; font-size: 17px; line-height: 1.55; }
  .contact--office { left: 44px; bottom: 40px; }
  .contact--direct { right: 44px; bottom: 40px; }
  .contact li { display: flex; align-items: center; gap: 10px; }
  .contact svg { width: 16px; height: 16px; fill: var(--accent-red); flex: none; }
</style>
</head>
<body>
  <section class="card card--front">
    <div class="brand"><span class="brand__dot"></span>Bramwell Ridge Minerals</div>
  </section>

  <section class="card card--back">
    <div class="brand"><span class="brand__dot"></span>Bramwell Ridge Minerals</div>

    <div class="person">
      <p class="person__name">DALE WHITCOMBE</p>
      <p class="person__role">General Manager</p>
    </div>

    <ul class="contact contact--office">
      <li>
        <svg viewBox="0 0 24 24" aria-hidden="true"><path d="M12 2a7 7 0 0 0-7 7c0 5 7 13 7 13s7-8 7-13a7 7 0 0 0-7-7zm0 9.5A2.5 2.5 0 1 1 12 6.5a2.5 2.5 0 0 1 0 5z"/></svg>
        1/3 first address, State. City ZIP
      </li>
      <li>
        <svg viewBox="0 0 24 24" aria-hidden="true"><path d="M2 5h20v14H2z M2 5l10 8 10-8" stroke="#3a3d42" stroke-width="1.5"/></svg>
        info@bramwellridgeminerals.com
      </li>
    </ul>

    <ul class="contact contact--direct">
      <li>
        <svg viewBox="0 0 24 24" aria-hidden="true"><path d="M6.6 10.8a15 15 0 0 0 6.6 6.6l2.2-2.2a1 1 0 0 1 1-.25 11.4 11.4 0 0 0 3.6.57 1 1 0 0 1 1 1V20a1 1 0 0 1-1 1A17 17 0 0 1 3 4a1 1 0 0 1 1-1h3.5a1 1 0 0 1 1 1c0 1.25.2 2.45.57 3.57a1 1 0 0 1-.25 1z"/></svg>
        +00 000 00 00 00
      </li>
      <li>
        <svg viewBox="0 0 24 24" aria-hidden="true"><path d="M6.6 10.8a15 15 0 0 0 6.6 6.6l2.2-2.2a1 1 0 0 1 1-.25 11.4 11.4 0 0 0 3.6.57 1 1 0 0 1 1 1V20a1 1 0 0 1-1 1A17 17 0 0 1 3 4a1 1 0 0 1 1-1h3.5a1 1 0 0 1 1 1c0 1.25.2 2.45.57 3.57a1 1 0 0 1-.25 1z"/></svg>
        +00 000 00 00 00
      </li>
      <li>
        <svg viewBox="0 0 24 24" aria-hidden="true"><path d="M2 5h20v14H2z M2 5l10 8 10-8" stroke="#3a3d42" stroke-width="1.5"/></svg>
        info@dalewhitcombe.com
      </li>
    </ul>
  </section>
</body>
</html>
```